Information One Page for Email

I am looking for a informative attachment I can send with an introductive email for Ridgeview Cable Works. Something I can also Mail.

Ridgeview Cable Works is the leader in Rebar Post Tension Cable Placement and Post Tension Cable repair. Outside of cable placement and repair we do concrete repair, Parking Garage restoration and

Content

Post Tension Repair and Concrete Restoration
Post-tensioning is a revolutionary method in concrete construction that enhances the strength and durability of structures. However, like all construction ele-ments, post-tension cables can experience wear and damage over time. Ensuring timely and effective repair is crucial for maintaining the safety and integrity of your building.
Why Post-Tension Cable Repair is Essential
1. **Structural Integrity**: Damaged or deteriorated cables can compromise the structural integrity of your building, leading to safety hazards and potential structural failures.
2. **Extended Lifespan**: Regular maintenance and repair of post-tension cables extend the lifespan of your structure, ensuring it remains safe and function-al for years to come.
3. **Cost-Effective**: Addressing cable issues early on prevents more severe damage and costly repairs down the line.
Common Signs of Post-Tension Cable Issues
- Cracks in concrete surfaces
- Unusual noises or popping sounds
- Visible cable ends or broken strands
- Water leakage through cracks
Our Repair Process
1. **Inspection and Assessment**: Our team conducts a thorough inspection to identify the extent of the damage and determine the appropriate repair meth-ods.
2. **Cable Repair or Replacement**: Depending on the severity, we either re-pair the existing cables or replace them with new ones to restore full functional-ity.
3. **Sealing and Protection**: After repairing, we seal the affected areas to protect against moisture and future damage.
4. **Quality Assurance**: We perform rigorous quality checks to ensure the repairs meet industry standards and the structure is safe for use.
Why Choose Us
- **Expertise and Experience**: With years of experience in post-tension cable repair, our team is skilled in handling even the most complex repairs efficiently and effectively.
- **Advanced Technology**: We use the latest technology and materials to ensure durable and long-lasting repairs.
- **Customer Satisfaction**: Our commitment to quality and customer satisfaction sets us apart. We work closely with our clients to ensure their needs are met and expectations exceeded.
Contact Us
If you suspect issues with your post-tension cables or need a routine inspection, don't hesitate to contact us. Our experts are ready to provide the best solutions to keep your structures safe and secure.
Ensure the safety and longevity of your building with our professional post-tension cable repair services. Trust us to deliver quality and reliability every time.

```html
<!DOCTYPE html>
<html lang="en">
<head>
<meta charset="UTF-8">
<title>Ridgeview Cable Works – Tension Repair and Concrete Restoration</title>
<link href="https://fonts.googleapis.com/css2?family=Poppins:wght@400;500;600;700&family=Arimo:wght@400;700&display=swap" rel="stylesheet">
<style>
  :root {
    --backdrop: #404040;
    --paper: #ececec;
    --green: #13673d;
    --ink: #0d0d0d;
    --white: #ffffff;
    --card: #fbfbfb;
    --card-head: #555555;
    --card-text: #6a6a6a;
  }
  * { margin: 0; padding: 0; box-sizing: border-box; }
  html, body { width: 910px; height: 1200px; overflow: hidden; background: var(--backdrop); }
  .sheet {
    position: absolute; left: 106px; top: 106px; width: 698px; height: 988px;
    background: var(--paper); overflow: hidden; font-family: 'Poppins', sans-serif; color: var(--ink);
  }
  .hero-photo { position: absolute; left: 0; top: 0; width: 698px; height: 284px; }
  .headline {
    position: absolute; left: 44px; top: 36px; font-weight: 700; font-size: 52px;
    line-height: 49px; letter-spacing: -0.3px;
  }
  .headline .accent { color: var(--green); }
  .intro {
    position: absolute; left: 44px; top: 192px; width: 353px; font-size: 11.3px;
    line-height: 12.7px; text-align: justify;
  }
  .why-band {
    position: absolute; left: 0; top: 284px; width: 698px; height: 413px;
    background: var(--green); color: var(--white);
  }
  .why-band h2 {
    position: absolute; left: 44px; top: 42px; font-size: 24.5px; font-weight: 600; letter-spacing: -0.2px;
  }
  .reason { position: absolute; left: 44px; width: 610px; font-size: 11px; line-height: 12.7px; }
  .reason strong { display: block; font-weight: 600; }
  .signs { position: absolute; left: 44px; top: 255px; list-style: none; font-size: 11px; line-height: 12.7px; }
  .cards { position: absolute; left: 44.5px; top: 637px; display: flex; gap: 15px; }
  .card {
    width: 192px; height: 211px; background: var(--card); padding: 10px 12px;
    box-shadow: 2px 3px 6px rgba(0,0,0,0.22); font-family: 'Arimo', sans-serif;
    color: var(--card-text); font-size: 9.2px; line-height: 13.3px;
  }
  .card h3 { font-size: 15px; font-weight: 700; color: var(--card-head); margin: 2px 0 9px; line-height: 18px; }
  .card ul { padding-left: 13px; }
  .card ul ul { padding-left: 13px; }
  .card p { margin-bottom: 13px; }
  .card ul + p { margin-top: 13px; }
  .brand {
    position: absolute; left: 44px; top: 893px; display: flex; align-items: center; gap: 8px;
    font-weight: 600; font-size: 19px; color: var(--green);
  }
  .brand .mark { width: 14px; height: 14px; background: var(--green); }
  .closing {
    position: absolute; left: 299px; top: 878px; width: 309px; font-size: 7.2px;
    line-height: 8.5px; text-align: justify; text-align-last: right;
  }
  .call {
    position: absolute; right: 47px; top: 917px; font-size: 25px; font-weight: 700;
    color: var(--green); letter-spacing: 0.2px;
  }
</style>
</head>
<body>
<main class="sheet">
  <svg class="hero-photo" viewBox="0 0 698 284" role="img" aria-label="Photo of a high-rise concrete building with shored, damaged balcony slabs under restoration">
    <defs>
      <linearGradient id="concrete" x1="0" y1="0" x2="1" y2="1">
        <stop offset="0" stop-color="#cfcdc8"/>
        <stop offset="0.5" stop-color="#a9a69f"/>
        <stop offset="1" stop-color="#7e7b74"/>
      </linearGradient>
    </defs>
    <polygon points="491,0 698,0 698,284 409,284" fill="url(#concrete)"/>
  </svg>

  <h1 class="headline">Tension Repair<br>and <span class="accent">Concrete<br>Restoration</span></h1>

  <p class="intro">Post-tensioning is a revolutionary method in concrete construction that enhances the strength and durability of structures. However, like all construction ele-ments, post-tension cables can experience wear and damage over time. Ensuring timely and effective repair is crucial for maintaining the safety and integrity of your building.</p>

  <section class="why-band">
    <h2>Why Post-Tension Cable Repair is Essential</h2>
    <p class="reason" style="top:91px"><strong>Structural Integrity</strong>Damaged or deteriorated cables can compromise the structural integrity of your building, leading to safety hazards and potential structural failures.</p>
    <p class="reason" style="top:142px"><strong>Extended Lifespan</strong>Regular maintenance and repair of post-tension cables extend the lifespan of your structure, ensuring it remains safe and function-al for years to come.</p>
    <p class="reason" style="top:205px"><strong>Cost-Effective</strong>Addressing cable issues early on prevents more severe damage and costly repairs down the line.<br>Common Signs of Post-Tension Cable Issues</p>
    <ul class="signs">
      <li>- Cracks in concrete surfaces</li>
      <li>- Unusual noises or popping sounds</li>
      <li>- Visible cable ends or broken strands</li>
      <li>- Water leakage through cracks</li>
    </ul>
  </section>

  <div class="cards">
    <article class="card">
      <h3>Services</h3>
      <ul>
        <li>Post Tension Repair</li>
        <li>Post Tension Restoration</li>
        <li>New Construction Reinforcing Installation</li>
        <li>Post Tension Consulting</li>
        <li>GPR Ground Penetrating Radar</li>
        <li>Barrier Cable:
          <ul>
            <li>Supply</li>
            <li>Install</li>
            <li>Replace</li>
            <li>Design &amp; Consulting</li>
          </ul>
        </li>
      </ul>
    </article>
    <article class="card">
      <h3>Project Specialties</h3>
      <p>Helping Contractors, Condo Associations, Property Managers &amp; Developers with their construction projects including:</p>
      <ul>
        <li>High Rise Office Buildings</li>
        <li>Parking Garages</li>
        <li>Condominiums
          <ul>
            <li>New Construction</li>
            <li>Restoration</li>
          </ul>
        </li>
        <li>Post Tension Slab on Grade</li>
      </ul>
    </article>
    <article class="card">
      <h3>Licensed &amp; Certified</h3>
      <ul>
        <li>PTI certified</li>
        <li>State GC Licensed</li>
        <li>Bonded and Insured</li>
        <li>CGC 1500482</li>
      </ul>
      <p>Certifications in Safety Include:</p>
      <ul>
        <li>30 hour OSHA</li>
        <li>Crane rigging and signaling</li>
        <li>Lull Operator</li>
      </ul>
    </article>
  </div>

  <div class="brand"><span class="mark"></span>Ridgeview Cable Works</div>

  <p class="closing">If you suspect issues with your post-tension cables or need a routine inspection, don't hesitate to contact us. Our experts are ready to provide the best solutions to keep your structures safe and secure. Ensure the safety and longevity of your building with our professional post-tension cable repair services. Trust us to deliver quality and reliability every time.</p>

  <p class="call">CALL (555) 201-4780</p>
</main>
</body>
</html>
```